Electrician Letterhead Design RMV

We need some letterhead for our bills and other papers.
Customer address is on the right side (Swiss format)
A4 format

Design should also be applicable on Cards

Target Market(s)

Private Customers, Small Business

Industry/Entity Type

Electrician

Other font styles liked:
• incised 901

Colors
00AB8E
00BBA5
67D7C9
C6EFE9
E9F9F6

```html
<!DOCTYPE html>
<html lang="en">
<head>
<meta charset="utf-8">
<title>RMV Letterhead</title>
<link rel="stylesheet" href="https://fonts.googleapis.com/css2?family=Lato:wght@400;700&family=Montserrat:wght@400;700&family=Parisienne&display=swap">
<style>
  :root {
    --teal: #039a88;
    --teal-light: #c6efe9;
    --ink: #2f2f2f;
    --ink-dark: #1c1c1c;
    --paper: #f6f6f6;
    --backdrop: #e2e2e2;
  }
  * { margin: 0; padding: 0; box-sizing: border-box; }
  html, body { width: 1153px; height: 1200px; overflow: hidden; background: var(--backdrop); }
  .letterhead {
    position: absolute; left: 166px; top: 26px; width: 820px; height: 1148px;
    background: radial-gradient(circle at 50% 35%, #ffffff 0%, var(--paper) 45%, #f1f1f1 100%);
    font-family: "Lato", sans-serif; color: var(--ink); overflow: hidden;
  }
  .brand { position: absolute; left: 61px; top: 50px; }
  .brand-name {
    font-family: "Montserrat", sans-serif; font-weight: 700; font-size: 80px;
    line-height: 1; color: var(--teal); letter-spacing: 1px;
  }
  .brand-sub {
    font-family: "Montserrat", sans-serif; font-weight: 700; font-size: 11.5px;
    color: var(--ink-dark); margin-top: 4px; letter-spacing: 0.3px;
  }
  .contact {
    position: absolute; left: 559px; top: 52px; padding-left: 10px;
    border-left: 1.5px solid var(--teal);
    font-family: "Montserrat", sans-serif; font-size: 13.3px; color: var(--ink-dark); line-height: 18px;
  }
  .contact-address { margin-bottom: 7px; }
  .contact-row { display: flex; align-items: center; gap: 6px; height: 19.5px; }
  .contact-icon { width: 12px; height: 12px; fill: var(--teal); flex: none; }
  .letter { position: absolute; left: 63px; width: 694px; font-size: 15.6px; line-height: 18.6px; }
  .date { top: 253px; }
  .recipient { top: 291px; }
  .recipient-company { margin-top: 18px; }
  .salutation { top: 427px; font-weight: 700; font-size: 19px; }
  .body { top: 468px; text-align: justify; line-height: 17.6px; letter-spacing: 0.1px; }
  .body p + p { margin-top: 17px; }
  .closing { top: 788px; }
  .signature {
    top: 833px; font-family: "Parisienne", cursive; font-size: 38px; line-height: 1;
    color: var(--ink-dark); width: auto;
  }
  .footer-band {
    position: absolute; left: 0; right: 0; top: 900px; bottom: 0;
    background: linear-gradient(180deg, rgba(198, 239, 233, 0) 0%, var(--teal-light) 25%, var(--teal) 70%);
  }
</style>
</head>
<body>
  <div class="letterhead">
    <div class="brand">
      <div class="brand-name">RMV</div>
      <div class="brand-sub">Elektrotechnik Rauber GmbH</div>
    </div>

    <div class="contact">
      <div class="contact-address">42-07 Larch Street 14,<br>Millbrook, NY 12545</div>
      <div class="contact-row">
        <svg class="contact-icon" viewBox="0 0 12 12"><path d="M1 4 Q6 0 11 4 L10 5.5 L8 4.5 L8 3.5 Q6 2.8 4 3.5 L4 4.5 L2 5.5 Z M3 6 H9 L10 10 H2 Z"/></svg>
        <span>555-318-2046</span>
      </div>
      <div class="contact-row">
        <svg class="contact-icon" viewBox="0 0 12 12"><path d="M1 3 H11 V9 H1 Z"/><path d="M1 3 L6 6.5 L11 3" stroke="#fff" stroke-width="1" fill="none"/></svg>
        <span>office@rmvmail.com</span>
      </div>
      <div class="contact-row">
        <svg class="contact-icon" viewBox="0 0 12 12"><circle cx="6" cy="6" r="5.2"/><path d="M3 4 Q5 3 6 5 Q5 7 3.5 7 Z M7 6.5 Q9 6 9.5 8 Q8 9.5 7 9 Z" fill="#fff"/></svg>
        <span>www.rmvelectric.com</span>
      </div>
    </div>

    <div class="letter date">Feb-03-2022</div>
    <div class="letter recipient">
      <div>Mr, Peter Lane<br>President</div>
      <div class="recipient-company">Harbor Works Ltd<br>123 Street Name, Suite# 10<br>City, State, 120023</div>
    </div>
    <div class="letter salutation">Dear Mr, Peter</div>
    <div class="letter body">
      <p>Lorem ipsum dolor sit amet, consectetur adipisicing elit, sed do eiusmod tempor incididunt ut labore et dolore magna aliqua. Ut enim ad minim veniam, quis nostrud exercitation ullamco laboris nisi ut aliquip ex ea commodo consequat. Duis aute irure dolor in reprehenderit in voluptate velit esse cillum dolore eu fugiat nulla pariatur.</p>
      <p>Lorem ipsum dolor sit amet, consectetur adipisicing elit, sed do eiusmod tempor incididunt ut labore et dolore magna aliqua. Ut enim ad minim veniam, quis nostrud exercitation ullamco laboris nisi ut aliquip ex ea commodo consequat. Duis aute irure dolor in reprehenderit in voluptate velit esse cillum dolore eu fugiat nulla pariatur.</p>
      <p>Lorem ipsum dolor sit amet, consectetur adipisicing elit, sed do eiusmod tempor incididunt ut labore et dolore magna aliqua. Ut enim ad minim veniam, quis nostrud exercitation ullamco laboris nisi ut aliquip ex ea commodo consequat.</p>
      <p>Excepteur sint occaecat cupidatat non proident, sunt in culpa qui officia deserunt mollit anim id est laborum. re et dolore magnam aliquam quaerat voluptatem.</p>
    </div>
    <div class="letter closing">Regards</div>
    <div class="letter signature">Daniel Moore</div>

    <div class="footer-band" role="img" aria-label="Decorative teal wave band along the foot of the page"></div>
  </div>
</body>
</html>
```